依頼詳細
・高級感、シンプルさ、オシャレな感じ、ポップな感じ、
はな凪や夕凪の鼓笛・雅之丞などの統一デザインっぽさ、
など方向性は自由です。
・洋風、和風など自由です。
・写真、イラスト、フォント自由です。筆文字可。(版権等にご注意ください。)
・色も自由です。金色銀色使用可能です。

良いと思うデザイン例
・コンセプトやデザインに一捻りあるもの。
(絶対に必要というわけではありません。)
・特別感。(絶対に必要というわけではありません。)
・贈答用に使える
・鶴かめ大漁をモチーフにしている。(絶対に必要というわけではありません。)

悪いと思うデザイン例
・スーパーによく置いてあるような安っぽい感じ。

印刷適正・文字などはデザイン決定後こちらで調整致しますので
背景や全体のデザインイメージを重要視します。

・ご提案をして頂く際に、ペットボトル・3㎏・4.5㎏のいずれかの
ご提案で判断したいと考えております。
記載項目
ペットボトル:W205×H100mm
3㎏サイズ:W260×H390mm
4.5㎏サイズ:W295×H460mm
グラビア印刷/ラミネート加工

```html
<!DOCTYPE html>
<html lang="ja">
<head>
<meta charset="utf-8">
<title>燦々米 3kg</title>
<link rel="stylesheet" href="https://fonts.googleapis.com/css2?family=Noto+Sans+JP:wght@300;400;500&display=swap">
<style>
  :root {
    --sky: #a9dbe9;
    --olive: #a39d6c;
    --ink: #3b3b3b;
    --paper: #f6f6f2;
  }
  html, body {
    margin: 0;
    width: 893px;
    height: 1200px;
    overflow: hidden;
    background: var(--paper);
  }
  p, h1 { margin: 0; }
  .package {
    position: relative;
    width: 893px;
    height: 1200px;
    font-family: "Noto Sans JP", sans-serif;
    color: var(--ink);
  }
  .band { position: absolute; left: 0; width: 100%; }
  .band--sky { top: 0; height: 670px; background: var(--sky); }
  .band--earth { top: 670px; height: 530px; background: var(--olive); }
  .variety {
    position: absolute; top: 28px; left: 0; width: 100%;
    text-align: center; font-size: 26px; letter-spacing: 2px;
  }
  .tagline {
    position: absolute; top: 395px; left: 0; width: 100%;
    text-align: center; font-size: 30px; letter-spacing: 6px;
  }
  .brand-name {
    position: absolute; top: 450px; left: 0; width: 100%;
    text-align: center; font-size: 190px; font-weight: 400;
    line-height: 1; letter-spacing: 10px; color: var(--ink);
  }
  .reading {
    position: absolute; top: 720px; left: 0; width: 100%;
    text-align: center; font-size: 34px; letter-spacing: 18px;
  }
  .weight {
    position: absolute; top: 975px; left: 0; width: 100%;
    text-align: center; font-size: 30px; letter-spacing: 6px;
  }
</style>
</head>
<body>
  <main class="package">
    <div class="band band--sky" role="img" aria-label="淡い青の波模様"></div>
    <div class="band band--earth" role="img" aria-label="落ち着いた黄土色の波模様"></div>

    <p class="variety">□□産ミルキーレイン</p>
    <p class="tagline">カメ殿が育てたお米</p>
    <h1 class="brand-name">燦々米</h1>
    <p class="reading">san san mai</p>
    <p class="weight">3kg</p>
  </main>
</body>
</html>
```